Professional Business Card for Commercial Cleaning Company

We need a business card that represents our commercial janitorial cleaning company and represent several brands for our company so we do not want to highlight the logo too much. We want something that says we are professional.
Notes:No website or address as we have many locations and many websites and companies under our corporate name of "Brightvale Holdings, LLC" . Every time we hand a customer a business card they have contacted us via another brand we own but we don't want to have 21 business cards so we want to not focus on Brightvale Holdings, LLC too much since people will automatically ask "What is Brightvale Holdings, LLC" Example: Noodle Barn and Wrap Lantern restaurants are owned by "Zest! Brands" is the corporation name. Same principle here. Except we do not advertise at this time that all of our brands are connected. Hope this helps.
Target Market(s)
Commercial Cleaning
Industry/Entity Type
Janitorial Service
Contact Information for Business Card
Milo Jarvis
Business Development
555-382-9047
sales@brightvaleholdingsllc.example
Requirements
Must have
- Logo with contact information, need to be able to easily edit contact info for others in my office.
Nice to have
- Professional Image. Like to see a colorful bold look and a more standard business card look.
Should not have
- Any type of cleaning icons, tools, people or water.

```html
<!DOCTYPE html>
<html lang="en">
<head>
<meta charset="utf-8">
<title>Brightvale Holdings, LLC — Business Card</title>
<link rel="stylesheet" href="https://fonts.googleapis.com/css2?family=Open+Sans:wght@400;600&display=swap">
<style>
  :root {
    --navy: #1f4a86;
    --navy-deep: #173b70;
    --navy-light: #2d5a96;
    --green: #6aae3f;
    --paper: #f4f5f7;
    --white: #ffffff;
    --backdrop: #d9d9d9;
    --text-font: "Open Sans", Arial, sans-serif;
  }
  * { box-sizing: border-box; margin: 0; padding: 0; }
  html, body {
    width: 1200px; height: 864px; overflow: hidden;
    background: var(--backdrop);
    font-family: var(--text-font);
  }
  .canvas {
    width: 1200px; height: 864px;
    display: flex; align-items: center; justify-content: center; gap: 40px;
  }
  .card {
    position: relative;
    width: 540px; height: 309px;
    overflow: hidden;
    box-shadow: 0 6px 18px rgba(0,0,0,.18);
  }
  .brand-name {
    font-weight: 600;
    color: var(--navy);
    letter-spacing: .3px;
    white-space: nowrap;
    text-align: center;
  }

  /* Front */
  .card-front { background: var(--paper); }
  .card-front .brand-name {
    position: absolute; left: 0; right: 0; top: 66px;
    font-size: 22px; line-height: 30px;
  }
  .front-band {
    position: absolute; left: 0; right: 0; top: 128px; height: 118px;
    background: radial-gradient(ellipse at 40% 50%, var(--navy-light), var(--navy-deep) 75%);
  }
  .rule {
    position: absolute; left: 0; right: 0; height: 3px; background: var(--navy);
  }
  .front-rule-top { top: 120px; }
  .front-rule-bottom { top: 251px; }
  .contact-list {
    position: absolute; left: 24px; top: 22px;
    list-style: none; color: var(--white); font-size: 14px; line-height: 22px;
  }
  .contact-list li { display: flex; align-items: center; gap: 8px; }
  .contact-icon { width: 12px; height: 12px; flex: none; }
  .person {
    position: absolute; right: 24px; bottom: 14px; text-align: right;
  }
  .person-name { color: var(--white); font-weight: 600; font-size: 19px; line-height: 24px; }
  .person-title { color: var(--green); font-size: 13px; line-height: 18px; }

  /* Back */
  .card-back { background: var(--navy); }
  .back-band {
    position: absolute; left: 0; right: 0; top: 70px; height: 114px;
    background: var(--paper);
  }
  .back-rule-top { top: 78px; }
  .back-rule-bottom { top: 173px; }
  .card-back .brand-name {
    position: absolute; left: 0; right: 0; top: 112px;
    font-size: 22px; line-height: 30px;
  }
</style>
</head>
<body>
<main class="canvas">

  <section class="card card-front" aria-label="Business card front">
    <div class="brand-name">Brightvale Holdings, LLC</div>
    <div class="rule front-rule-top"></div>
    <div class="front-band">
      <ul class="contact-list">
        <li>
          <svg class="contact-icon" viewBox="0 0 12 12" aria-hidden="true">
            <rect width="12" height="12" fill="var(--green)"/>
            <path d="M3.5 2.5l1.5 1.8-.8 1c.5 1 1.3 1.8 2.3 2.3l1-.8 1.8 1.5-.9 1.2C5.8 9.3 2.7 6.2 2.5 3.4z" fill="#fff"/>
          </svg>
          555-382-9047
        </li>
        <li>
          <svg class="contact-icon" viewBox="0 0 12 12" aria-hidden="true">
            <rect width="12" height="12" fill="var(--green)"/>
            <rect x="2.5" y="3.5" width="7" height="5" fill="none" stroke="#fff" stroke-width="1"/>
            <path d="M2.5 3.5L6 6.3l3.5-2.8" fill="none" stroke="#fff" stroke-width="1"/>
          </svg>
          sales@brightvaleholdingsllc.example
        </li>
      </ul>
      <div class="person">
        <div class="person-name">Milo Jarvis</div>
        <div class="person-title">Business Development</div>
      </div>
    </div>
    <div class="rule front-rule-bottom"></div>
  </section>

  <section class="card card-back" aria-label="Business card back">
    <div class="back-band"></div>
    <div class="rule back-rule-top"></div>
    <div class="rule back-rule-bottom"></div>
    <div class="brand-name">Brightvale Holdings, LLC</div>
  </section>

</main>
</body>
</html>
```